Aged Care Consultancy Business needs a business card design

I need a two sided business card - I want it clean and professional. Surprise me

Target Market(s)

middle aged and ageing victorians

Industry/Entity Type

Health Care

Contact Information for Business Card

Text to be included

Logo
Aged Care Consulting Services
Professional, Reliable, Affordable

Orin Tessaldo
Director
0472 31 64 09 (larger)
1300 31 64 09
orin@valtrino.com.au
www.valtrinocare.com.au
Facebook (details TBA)

include little icons beside the contact info:

- Envelope = email
- Phone = phone
- Globe = website

Font styles to use
Serif
Sans Serif

Requirements
Must have
• look proffesional and clean

```html
<!DOCTYPE html>
<html lang="en">
<head>
<meta charset="utf-8">
<title>Valtrino Care – Business Card</title>
<link href="https://fonts.googleapis.com/css2?family=Questrial&display=swap" rel="stylesheet">
<style>
  :root {
    --navy: #223f7a;
    --navy-card: #1d3f78;
    --orange: #e68a22;
    --backdrop: #b1b1b1;
    --card-light: #f7f7f7;
    --card-edge: #e4e4e4;
    --white: #ffffff;
  }
  html, body {
    margin: 0;
    padding: 0;
    width: 1200px;
    height: 1050px;
    overflow: hidden;
    background: var(--backdrop);
    font-family: "Questrial", "Century Gothic", sans-serif;
  }
  .canvas { position: relative; width: 1200px; height: 1050px; }
  .card {
    position: absolute;
    left: 264px;
    width: 672px;
    height: 383px;
    border-radius: 40px;
    overflow: hidden;
  }
  .card--front {
    top: 111px;
    background: radial-gradient(ellipse at 55% 45%, var(--white) 0%, var(--card-light) 55%, var(--card-edge) 100%);
  }
  .card--back {
    top: 573px;
    background: radial-gradient(ellipse at 50% 45%, #214680 0%, var(--navy-card) 70%, #1a386c 100%);
  }
  .brand {
    position: absolute;
    display: flex;
    align-items: center;
    gap: 12px;
    white-space: nowrap;
    line-height: 1;
  }
  .brand__dot { border-radius: 50%; background: var(--orange); flex: none; }
  .card--front .brand { left: 90px; top: 176px; font-size: 44px; color: var(--navy); }
  .card--front .brand__dot { width: 22px; height: 22px; }
  .tagline {
    position: absolute;
    left: 87px;
    top: 250px;
    font-size: 14px;
    color: var(--navy);
    white-space: nowrap;
  }
  .tagline em { font-style: normal; color: var(--orange); }
  .person { position: absolute; left: 374px; top: 78px; }
  .person__name { font-size: 23px; color: var(--orange); line-height: 1.1; }
  .person__role { font-size: 16px; color: var(--navy); margin-top: 2px; }
  .contacts {
    position: absolute;
    left: 375px;
    top: 156px;
    margin: 0;
    padding: 0;
    list-style: none;
  }
  .contacts li {
    display: flex;
    align-items: center;
    gap: 10px;
    height: 20px;
    font-size: 16px;
    color: var(--navy);
    white-space: nowrap;
  }
  .contacts svg { width: 16px; height: 16px; flex: none; }
  .contacts .accent { color: var(--orange); }
  .address {
    position: absolute;
    left: 375px;
    top: 268px;
    font-size: 16px;
    line-height: 19px;
    color: var(--navy);
  }
  .card--back .brand {
    left: 0; right: 0; top: 150px;
    justify-content: center;
    font-size: 54px;
    color: var(--white);
  }
  .card--back .brand__dot { width: 26px; height: 26px; }
  .social {
    position: absolute;
    left: 0; right: 0; top: 348px;
    text-align: center;
    font-size: 16px;
    color: #e9edf5;
  }
</style>
</head>
<body>
<main class="canvas">
  <section class="card card--front" aria-label="Card front">
    <div class="brand"><span class="brand__dot"></span><span class="brand__name">valtrino care</span></div>
    <p class="tagline" style="margin:0">Professional, <em>Reliable</em>, Affordable</p>

    <div class="person">
      <div class="person__name">Orin Tessaldo</div>
      <div class="person__role">Director</div>
    </div>

    <ul class="contacts">
      <li>
        <svg viewBox="0 0 16 16" aria-hidden="true"><rect x="2" y="1" width="12" height="14" rx="1.5" fill="var(--orange)"/><rect x="4" y="3" width="2" height="10" fill="#fff"/><rect x="8" y="3" width="4" height="3" fill="#fff"/></svg>
        0472 31 64 09
      </li>
      <li>
        <svg viewBox="0 0 16 16" aria-hidden="true"><path d="M3.5 1.5l2.5 0 1 3.5-1.8 1.3a8 8 0 0 0 4.5 4.5l1.3-1.8 3.5 1v2.5c0 .8-.7 1.5-1.5 1.5C7 14 2 9 2 3c0-.8.7-1.5 1.5-1.5z" fill="var(--orange)"/></svg>
        1300 31 64 09
      </li>
      <li>
        <svg viewBox="0 0 16 16" aria-hidden="true"><rect x="1" y="3" width="14" height="10" fill="var(--orange)"/><path d="M1.5 3.5L8 9l6.5-5.5M1.5 12.5l5-4.5M14.5 12.5l-5-4.5" stroke="#fff" stroke-width="1.2" fill="none"/></svg>
        orin@valtrino.com.au
      </li>
      <li>
        <svg viewBox="0 0 16 16" aria-hidden="true"><g fill="none" stroke="var(--orange)" stroke-width="1.2"><circle cx="8" cy="8" r="6.5"/><ellipse cx="8" cy="8" rx="3" ry="6.5"/><path d="M1.5 8h13M2.5 5h11M2.5 11h11"/></g></svg>
        <span>www.<span class="accent">valtrinocare</span>.com.au</span>
      </li>
    </ul>

    <p class="address" style="margin:0">Here your company<br>or home address</p>
  </section>

  <section class="card card--back" aria-label="Card back">
    <div class="brand"><span class="brand__dot"></span><span class="brand__name">valtrino care</span></div>
    <p class="social" style="margin:0">www.socialpage.com.au/valtrinocare</p>
  </section>
</main>
</body>
</html>
```